Corporate Design für Lindmar Naturwerk
Die Desgins sind wunderschön geworden. Die Kommunikation war stets sehr freundlich und schnell. Wir freuen uns auf die auch weiterhin bestehende und Zukünftige Zusammenarbeit.
Zielgruppe
Verkauf von diversen hoch qualitativen Honigprodukten. Produktion eigener Honig Produkte unter der Marke Lindmar Naturwerk.
Online Shop in der Schweiz
Aufgabenstellung
Das Logo soll aus einer Krone mit Gold-Schwarzen Bienen Streifen sein. Das ganze Design soll Bezug zu Honig und Bienen haben.
Wir sind offen für diverse Ideen. (evtl. auch Bezug zu Schweiz)

```html
<!DOCTYPE html>
<html lang="de">
<head>
<meta charset="utf-8">
<title>Lindmar Naturwerk – Geschäftsausstattung</title>
<link rel="stylesheet" href="https://fonts.googleapis.com/css2?family=Alegreya:wght@400;700&display=swap">
<style>
  :root {
    --backdrop: #e7e3dc;
    --paper: #ffffff;
    --ink: #1f1f1f;
    --honey: #f0a81c;
    --honey-deep: #e58a12;
    --shadow: rgba(0, 0, 0, 0.28);
  }
  * { box-sizing: border-box; margin: 0; padding: 0; }
  html, body { width: 1200px; height: 1016px; overflow: hidden; }
  body {
    background: var(--backdrop);
    font-family: "Alegreya", Georgia, serif;
    color: var(--ink);
    position: relative;
  }
  .sheet {
    position: absolute;
    background: var(--paper);
    box-shadow: 0 4px 14px var(--shadow);
  }
  .letterhead { left: 37px; top: 55px; width: 656px; height: 906px; font-size: 9.3px; line-height: 15.5px; }
  .letterhead > * { position: absolute; }

  .brand-mark { display: flex; flex-direction: column; align-items: center; gap: 8px; }
  .brand-mark .dot { width: 18px; height: 18px; border-radius: 50%; background: var(--honey); }
  .brand-mark .name { font-size: 19px; font-weight: 400; color: var(--ink); letter-spacing: 0.5px; white-space: nowrap; }

  .letterhead .brand-mark { left: 465px; top: 82px; width: 150px; }
  .sender-line { left: 77px; top: 131px; font-size: 7.4px; }
  .sender-line .sep { color: var(--honey); }
  .recipient { left: 77px; top: 160px; }
  .date { right: 64px; top: 254px; font-size: 7.6px; }
  .subject { left: 77px; top: 284px; font-weight: 700; }
  .body-copy { left: 77px; top: 314px; width: 440px; }
  .body-copy p { margin-bottom: 15.5px; }
  .body-copy p.tight { margin-bottom: 0; }
  .signature { left: 76px; top: 740px; width: 76px; height: 16px; background: linear-gradient(90deg, #3a3a3a 0%, #6a6a6a 100%); opacity: 0.18; border-radius: 3px; }
  .signer { left: 77px; top: 760px; }

  .footer { left: 77px; top: 830px; display: grid; grid-template-columns: 134px 135px 134px 134px; font-size: 7.6px; line-height: 12px; }

  .card { width: 406px; height: 262px; left: 756px; }
  .card-front { top: 203px; }
  .card-front .brand-mark { position: absolute; left: 225px; top: 135px; width: 150px; }
  .card-front .brand-mark .name { font-size: 18px; }

  .card-back { top: 552px; }
  .card-back .holder { position: absolute; left: 67px; top: 48px; font-size: 15.5px; font-weight: 700; }
  .card-back .holder .sep { color: var(--honey); }
  .card-back .contact { position: absolute; left: 67px; font-size: 12.3px; line-height: 18.5px; }
  .card-back .address { top: 93px; }
  .card-back .phone { top: 137px; }
  .card-back .online { top: 181px; }
  .card-back .mini-mark { position: absolute; left: 270px; top: 190px; display: flex; align-items: center; gap: 5px; font-size: 9px; color: var(--honey-deep); }
  .card-back .mini-mark .dot { width: 8px; height: 8px; border-radius: 50%; background: var(--honey); }
</style>
</head>
<body>

<section class="sheet letterhead">
  <div class="brand-mark">
    <span class="dot"></span>
    <span class="name">Lindmar Naturwerk</span>
  </div>

  <p class="sender-line">Max Muster <span class="sep">·</span> Musterstraße 1 <span class="sep">·</span> 23456 Musterstadt</p>

  <address class="recipient" style="font-style:normal">
    Bernd Beispiel<br>Beispielweg 7<br>89012 Beispielstadt
  </address>

  <p class="date">Musterstadt, TT. Monat JJJJ</p>

  <p class="subject">Stet clita kasd gubergren no sea</p>

  <div class="body-copy">
    <p>Sehr geehrter Herr Beispiel,</p>
    <p>lorem ipsum dolor sit amet, consetetur sadipscing elitr, sed diam nonumy eirmod tempor<br>invidunt ut labore et dolore magna aliquyam erat, sed diam voluptua.</p>
    <p>At vero eos et accusam et justo duo dolores et ea rebum. Stet clita kasd gubergren, no sea<br>takimata sanctus est Lorem ipsum dolor sit amet. Lorem ipsum dolor sit amet, consetetur<br>sadipscing elitr, sed diam nonumy eirmod tempor invidunt ut labore.</p>
    <p class="tight">Dolore magna aliquyam erat, sed diam voluptua. At vero eos et accusam et justo duo dolores<br>et ea rebum. Stet clita kasd gubergren, no sea takimata sanctus est Lorem ipsum dolor sit<br>amet.</p>
    <p class="tight">At vero eos et accusam et justo duo dolores et ea rebum. Stet clita kasd gubergren, no sea<br>takimata sanctus est Lorem ipsum dolor sit amet. Lorem ipsum dolor sit amet, consetetur<br>sadipscing elitr, sed diam nonumy eirmod tempor invidunt ut labore.</p>
    <p>Dolore magna aliquyam erat, sed diam voluptua. At vero eos et accusam et justo duo dolores<br>et ea rebum. Stet clita kasd gubergren, no sea takimata sanctus est Lorem ipsum dolor sit<br>amet. At vero eos et accusam et justo duo dolores et ea rebum. Stet clita kasd gubergren, no<br>sea takimata sanctus est Lorem ipsum dolor sit amet. Lorem ipsum dolor sit amet, consetetur<br>sadipscing elitr, sed diam nonumy eirmod tempor invidunt ut labore.</p>
    <p>Dolore magna aliquyam erat, sed diam voluptua. At vero eos et accusam et justo duo dolores<br>et ea rebum. Stet clita kasd gubergren, no sea takimata sanctus est Lorem ipsum dolor sit<br>amet.</p>
    <p>Mit freundlichen Grüßen,</p>
  </div>

  <div class="signature" role="img" aria-label="Handschriftliche Unterschrift von Max Muster"></div>
  <p class="signer">Max Muster</p>

  <footer class="footer">
    <div>Firmenname und Rechtsform<br>Geschäftsführer<br>Musterstraße 1<br>23456 Musterstadt</div>
    <div>Telefon 01234 567890<br>Fax 01234 567899<br>muster@muster.de<br>www.muster.de</div>
    <div>DE21 1234 5678 0000 0123 45<br>ABCD DE XX XXX<br>Ust-IdNr.<br>HRS-Nummer</div>
    <div>CH21 1234 5678 0000 0123 45<br>ABCD CH XX XXX<br>Ust-IdNr.<br>HRS-Nummer</div>
  </footer>
</section>

<section class="sheet card card-front">
  <div class="brand-mark">
    <span class="dot"></span>
    <span class="name">Lindmar Naturwerk</span>
  </div>
</section>

<section class="sheet card card-back">
  <p class="holder">Max Muster <span class="sep">·</span> Geschäftsführer</p>
  <p class="contact address">Musterstraße 1<br>23456 Musterstadt</p>
  <p class="contact phone">Telefon 01234 567890<br>Fax 01234 567899</p>
  <p class="contact online">muster@muster.de<br>www.muster.de</p>
  <div class="mini-mark"><span class="dot"></span><span>Lindmar Naturwerk</span></div>
</section>

</body>
</html>
```